Hong Kong residential leasing and sales company needs a website design

Hong Kong has many competitive real estate agents. The majority of us have the same listings so, besides the team and experience, a website is what makes us stand out. A first impression. We need our website to be user friendly, informative and to have a wow factor. Most sites are generic so whilst we are close to accepting that maybe that's the only formula which works....we would like to see if we're missing something! Our clients are a mix of International users of all ages but probably ultimately 35+.. We have a logo (attached) which we would like to keep - designed by artmarketly. Flexible with colours except red.
examples of our competitors are:
http://www.brindlewoodestates.example
http://www.nuvo.example/home
http://www.premierdwellingsvx.example
http://www.orchid-lettings.example
http://www.tidemark-harrowgates.example
We were thinking of having the following in a menu bar with drop downs for most...some more than others. Home / For Sale / For Rent / Property 101 / About us / Contact Us ..
Look forward to seeing your ideas. Thanks in advance.

```html
<!DOCTYPE html>
<html lang="en">
<head>
<meta charset="utf-8">
<title>Lumen Residences</title>
<link rel="stylesheet" href="https://fonts.googleapis.com/css2?family=Gelasio:wght@400;600&display=swap">
<style>
:root{
  --purple:#8a4ea3;
  --purple-dark:#6e3a86;
  --footer:#77428e;
  --ink:#3a3a3a;
  --muted:#666;
  --nav:#2e2b30;
  --btn-dark:#4a454d;
  --paper:#f3f3f3;
  --paper-2:#e6e6e6;
  --bottom:#2d2a2e;
  --white:#fff;
}
*{margin:0;padding:0;box-sizing:border-box}
html,body{width:750px;height:1200px;overflow:hidden}
body{position:relative;font-family:"Gelasio",Georgia,serif;color:var(--ink);background:var(--paper);letter-spacing:.06em}
.abs{position:absolute}

.hero{left:0;top:0;width:750px;height:458px;
  background:
    radial-gradient(ellipse 260px 150px at 260px 230px,rgba(235,240,240,.85),rgba(235,240,240,0) 100%),
    radial-gradient(ellipse 200px 60px at 320px 320px,rgba(240,236,226,.9),rgba(240,236,226,0) 100%),
    radial-gradient(ellipse 180px 160px at 680px 250px,rgba(60,42,30,.85),rgba(60,42,30,0) 100%),
    radial-gradient(ellipse 120px 200px at 20px 260px,rgba(90,78,66,.7),rgba(90,78,66,0) 100%),
    linear-gradient(180deg,#d8d2c6 0%,#bcc3c4 30%,#a9aeab 52%,#8a7a68 70%,#5a4533 85%,#3a2a20 100%)}
.language{right:38px;top:6px;font-size:9px;color:#fff;display:flex;align-items:center;gap:5px}
.language .flag{width:14px;height:9px;background:#2a3d7a;border:1px solid #fff}

.header{left:30px;top:24px;width:690px;height:78px;background:linear-gradient(#f7f7f7,#dcdcdc);box-shadow:0 2px 6px rgba(0,0,0,.35)}
.brand{left:46px;top:26px;display:flex;align-items:center;gap:7px;font-size:12px;color:var(--purple-dark);letter-spacing:.14em;font-weight:600}
.brand .mark{width:12px;height:12px;background:var(--purple)}
.socials{left:483px;top:14px;display:flex;gap:6px}
.socials span{width:16px;height:16px;border-radius:50%}
.search{left:574px;top:12px;width:102px;height:19px;border:1px solid #c8c8c8;background:#fff;font-size:8px;color:#aaa;padding:4px 6px}
.nav{left:234px;top:38px;width:456px;height:33px;background:var(--nav);display:flex;font-size:8.5px;color:#fff;letter-spacing:.09em}
.nav a{color:inherit;text-decoration:none;display:flex;align-items:center;padding:0 11px;border-right:1px solid #46424a}
.nav a:last-child{border:0}
.nav .active{background:var(--purple);padding:0 17px}

.welcome{left:48px;top:380px;width:649px;height:78px;background:rgba(138,78,163,.88);text-align:center;color:#fff}
.welcome h1{font-weight:400;font-size:14px;letter-spacing:.1em;margin-top:13px}
.welcome p{font-size:8.4px;line-height:11px;width:450px;margin:6px auto 0}
.welcome b{font-weight:600}

.section-title{font-size:13px;font-weight:400;letter-spacing:.1em;display:flex;align-items:center;gap:6px;color:var(--ink)}
.section-title::after{content:"";flex:1;height:1px;background:#c8c8c8}

.sale-title{left:46px;top:472px;width:652px}
.card{top:495px;width:154px;height:109px;background:#fff;border:1px solid #d8d8d8;padding:1px}
.card .photo{height:87px}
.card h3{font-weight:400;font-size:8.6px;color:var(--purple);letter-spacing:.1em;margin:5px 2px 0}
.btn{height:23px;font-size:8px;color:#fff;display:flex;align-items:center;justify-content:center;letter-spacing:.1em}
.btn.primary{background:var(--purple)}
.btn.dark{background:var(--btn-dark)}

.agents{left:0;top:696px;width:750px;height:285px;background:var(--paper-2)}
.agents-title{left:46px;top:707px;width:652px}
.agents-intro{left:135px;top:734px;width:450px;text-align:center;font-size:8.6px;line-height:11px;color:var(--muted)}
.agent{top:794px;width:110px;text-align:center;font-size:8.8px;color:var(--muted)}
.agent .portrait{width:72px;height:72px;margin:0 auto 9px;border-radius:50%;border:3px solid #9a9a9a;background:radial-gradient(circle at 50% 55%,#d8c2b0 0%,#c2a894 35%,#eeeeee 70%,#fafafa 100%)}

.footer{left:0;top:981px;width:750px;height:189px;background:var(--footer);color:#fff}
.col-title{top:1015px;font-size:10px;letter-spacing:.12em;font-weight:600;color:#fff}
.footer-rule{left:34px;top:1034px;width:670px;height:1px;background:rgba(255,255,255,.25)}
.links{top:1043px;list-style:none;font-size:8.8px;color:#fff}
.links li{height:20px;display:flex;align-items:center;gap:5px}
.links li::before{content:"→";font-size:9px}
.follow{left:280px;top:1043px;list-style:none;font-size:8.8px;color:#fff}
.follow li{height:26px;display:flex;align-items:center;gap:10px}
.follow .dot{width:16px;height:16px;border-radius:50%;background:#fff;opacity:.9}
.about-logo{left:390px;top:1041px;width:128px;height:99px;background:#fff;border:5px solid #5d3172;display:flex;align-items:center;justify-content:center;gap:6px;font-size:11px;font-weight:600;color:var(--purple-dark);letter-spacing:.1em}
.about-logo .mark{width:10px;height:10px;background:var(--purple)}
.about-text{left:530px;top:1040px;width:170px;font-size:8.6px;line-height:12px;text-align:justify;color:#fff}
.about-text p+p{margin-top:12px}
.bottom{left:0;top:1170px;width:750px;height:30px;background:var(--bottom);color:#ddd;font-size:9px;padding:8px 38px}
</style>
</head>
<body>
<div class="abs hero" role="img" aria-label="High-rise living room with white sofa and floor-to-ceiling windows over a city skyline"></div>
<div class="abs language">Language <span class="flag"></span></div>

<header class="abs header">
  <div class="abs brand"><span class="mark"></span>LUMEN RESIDENCES</div>
  <div class="abs socials">
    <span style="background:#3b5b9a"></span><span style="background:#4a95cf"></span><span style="background:#4d7a9c"></span><span style="background:#e08a2b"></span>
  </div>
  <div class="abs search">Search...</div>
  <nav class="abs nav">
    <a class="active" href="#">HOME</a><a href="#">FOR SALE</a><a href="#">FOR RENT</a><a href="#">PROPERTY 101</a><a href="#">ABOUT US</a><a href="#">CONTACT US</a>
  </nav>
</header>

<section class="abs welcome">
  <h1>WELCOME TO LUMEN RESIDENCES</h1>
  <p>Lorem ipsum dolor sit amet, consectetur adipiscing elit. Maecenas lectus leo, dapibus consectetur adipiscing elitimperdiet magna eu. consectetur adipiscing eli dapibus imperdiet magna eu. consectetur adipiscing elit. Maecenas lectus leo. <b>Read more &gt;</b></p>
</section>

<h2 class="abs section-title sale-title">FOR SALE</h2>
<article class="abs card" style="left:46px"><div class="photo" role="img" aria-label="Villa with swimming pool and garden" style="background:radial-gradient(ellipse 60px 25px at 60% 45%,rgba(236,226,190,.95),rgba(236,226,190,0)),linear-gradient(180deg,#4f7a32 0%,#7da24c 30%,#d9cfa8 55%,#e8e4d8 68%,#4fa3c6 80%,#2f86b0 100%)"></div><h3>PROPERTY NAME HERE</h3></article>
<article class="abs card" style="left:211px"><div class="photo" role="img" aria-label="Modern pavilion overlooking a pool and lawn" style="background:radial-gradient(ellipse 50px 45px at 80% 40%,rgba(246,244,238,.95),rgba(246,244,238,0)),linear-gradient(180deg,#3f93d6 0%,#8cc3ea 40%,#6f9a42 62%,#4a7a2c 78%,#2f7fa8 100%)"></div><h3>PROPERTY NAME HERE</h3></article>
<article class="abs card" style="left:377px"><div class="photo" role="img" aria-label="Bright open-plan kitchen and lounge" style="background:radial-gradient(ellipse 40px 20px at 75% 75%,rgba(70,150,170,.6),rgba(70,150,170,0)),linear-gradient(180deg,#f4f4f2 0%,#e6e4df 45%,#c9c4bb 65%,#8c7f72 85%,#6e6258 100%)"></div><h3>PROPERTY NAME HERE</h3></article>
<article class="abs card" style="left:542px"><div class="photo" role="img" aria-label="House lit at dusk with a blue pool" style="background:radial-gradient(ellipse 55px 30px at 50% 55%,rgba(230,190,120,.95),rgba(230,190,120,0)),linear-gradient(180deg,#1c2f58 0%,#2c4a7c 30%,#6b6a55 55%,#2b3a2a 72%,#2fa0d8 85%,#1a7ab8 100%)"></div><h3>PROPERTY NAME HERE</h3></article>

<a class="abs btn primary" style="left:210px;top:629px;width:158px">VIEW FOR RENT PROPERTIES</a>
<a class="abs btn dark" style="left:378px;top:629px;width:157px">VIEW FOR SALE PROPERTIES</a>

<section class="abs agents"></section>
<h2 class="abs section-title agents-title">FEAUTURED AGENTS</h2>
<p class="abs agents-intro">Lorem ipsum dolor sit amet, consectetur adipiscing elit. Maecenas lectus leo, dapibus consectetur adipiscing elitimperdiet magna eu. consectetur adipiscing eli dapibus imperdiet magna eu. consectetur adipiscing elit. Maecenas lectus leo.</p>
<div class="abs agent" style="left:82px"><div class="portrait" role="img" aria-label="Agent portrait"></div>Agent Name Here</div>
<div class="abs agent" style="left:198px"><div class="portrait" role="img" aria-label="Agent portrait"></div>Agent Name Here</div>
<div class="abs agent" style="left:313px"><div class="portrait" role="img" aria-label="Agent portrait"></div>Agent Name Here</div>
<div class="abs agent" style="left:429px"><div class="portrait" role="img" aria-label="Agent portrait"></div>Agent Name Here</div>
<div class="abs agent" style="left:544px"><div class="portrait" role="img" aria-label="Agent portrait"></div>Agent Name Here</div>
<a class="abs btn primary" style="left:293px;top:914px;width:157px">VIEW LIST OF OUR AGENTS</a>

<footer class="abs footer"></footer>
<h4 class="abs col-title" style="left:34px">QUICKLINKS</h4>
<h4 class="abs col-title" style="left:151px">USEFUL INFO</h4>
<h4 class="abs col-title" style="left:275px">FOLLOW US</h4>
<h4 class="abs col-title" style="left:390px">ABOUT US</h4>
<div class="abs footer-rule"></div>
<ul class="abs links" style="left:38px"><li>Home</li><li>For Sale</li><li>For Rent</li><li>Property 101</li><li>Contact us</li></ul>
<ul class="abs links" style="left:154px"><li>FAQ</li><li>Sitemap</li><li>Terms &amp; Agreement</li><li>Agents</li><li>Privacy Policy</li></ul>
<ul class="abs follow"><li><span class="dot"></span>Birdline</li><li><span class="dot"></span>Friendbook</li><li><span class="dot"></span>Snapgram</li><li><span class="dot"></span>Rss Feed</li></ul>
<div class="abs about-logo"><span class="mark"></span>LUMEN</div>
<div class="abs about-text">
  <p>Lorem ipsum dolor sit amet, consectetur adipiscing elit. Duis molestie augue eu metus dignissim aliquam semper semper sapien.</p>
  <p>Duis molestie augue eu metus dignissim aliquam semper semper sapien molestie augue eu metus digni.</p>
</div>
<div class="abs bottom">Copyright © 2014 Lumen Residences All rights reserved</div>
</body>
</html>
```